SIGN UP PAGE AND CHECK OUT PROCESS DESIGN NEEDED

I offer a subscription service. Two products that offer the same exact features just two different prices as the cheaper product offers limited of all the features....<br/><br/>PLEASE USE EXISTING THEME OF CURRENT DESIGN JUST MAKE AN IMPROVED SIGN UP PAGE. <br/><br/><br/>NEED SIGN UP PAGE for a subscription service..... <br/>This is my current sign up page, only offers one product: https://www.brightloomrewards.biz/?page=signup <br/><br/>Please use all the same fields and content listed on this sign up page also please do a fake sign up to see the credit card page. I also need the credit card page to be designed....or if you want to combine the sign up and credit card page, etc. all in one I am open for that too....my goal is a super quick an easy sign up for customer. <br/><br/> AL A CARTE PROGRAM<br/>1 CERTIFICATE TYPE EACH MONTH<br/>$49/MTH MONTH TO MONTH BASIS NO CONTRACTS<br/>$239 ONE TIME PAYMENT FOR 6 MTHS OF SERVICE<br/>$399 ONE TIME PAYMENT FOR 12 MONTHS OF SERVICE<br/><br/>FEATURES:<br/><br/>UNLIMITED CERTIFICATE PDF DOWNLOADS<br/><br/>UNLIMITED E-MAIL CERTIFICATES<br/><br/>UNLIMITED TEXT/SMS CERTIFICATES<br/><br/>UNLIMITED API USAGE<br/><br/>UNLIMITED WEB BANNER CERTIFICATES<br/><br/>FULL REDEMPTION TRACKING<br/><br/>CERTIFICATE DISTRIBUTION REPORTS<br/><br/>WHITE LABEL REDEMPTION SITE<br/><br/>END USER MARKETING VIDEOS<br/><br/>MARKETING POSTERS AND FLYERS<br/><br/>PRODUCT DESCRIPTIONI BROCHURES<br/><br/>THE LATEST TIPS<br/><br/>SEPERATE REDEMPTION WEBSITES<br/><br/>CONTACT US 24/7<br/><br/>AFFILIATE PROGRAM<br/><br/>DISCOUNT TRAVEL BOOKING ENGINE<br/><br/>UNLIMITED PROGRAM<br/>UNLIMITED AMOUNTS OF ALL THE CERTIFICATES<br/>$99/MTH MONTH TO MONTH BASIS NO CONTRACTS<br/>$495 ONE TIME PAYMENT FOR 6 MTHS OF SERVICE<br/>$2,295 ONE TIME PAYMENT FOR 12 MONTHS OF SERVICE<br/><br/>FEATURES:<br/><br/>UNLIMITED CERTIFICATE PDF DOWNLOADS<br/><br/>UNLIMITED E-MAIL CERTIFICATES<br/><br/>UNLIMITED TEXT/SMS CERTIFICATES<br/><br/>UNLIMITED API USAGE<br/><br/>UNLIMITED WEB BANNER CERTIFICATES<br/><br/>FULL REDEMPTION TRACKING<br/><br/>CERTIFICATE DISTRIBUTION REPORTS<br/><br/>WHITE LABEL REDEMPTION SITE<br/><br/>END USER MARKETING VIDEOS<br/><br/>MARKETING POSTERS AND FLYERS<br/><br/>PRODUCT DESCRIPTIONI BROCHURES<br/><br/>THE LATEST TIPS<br/><br/>SEPERATE REDEMPTION WEBSITES<br/><br/>CONTACT US 24/7<br/><br/>AFFILIATE PROGRAM<br/><br/>DISCOUNT TRAVEL BOOKING ENGINE<br/><br/><br/>

Target Market(s)

B2B SMALL BUSINESS OWNERS
MARKETERS
ADVERTISERS

Industry/Entity Type

Digital Marketing

Number of Pages Required

3 page

Colors

Designer to choose colors to be used in the design.

Requirements
Must have
• MUST MATCH EXISTING THEME
Nice to have
• A VERY MODERN DESIGN

```html
<!DOCTYPE html>
<html lang="en">
<head>
<meta charset="utf-8">
<title>Sign Up – Bright Loom Rewards</title>
<link href="https://fonts.googleapis.com/css2?family=Lato:wght@400;700&family=Montserrat:wght@500;600;700&family=Poppins:wght@400;500&display=swap" rel="stylesheet">
<style>
:root{
  --ink:#1c1c1c;
  --header:#1f1f1f;
  --footer:#1d1d1d;
  --footer-base:#121212;
  --blue:#0b72c5;
  --navy:#071b2c;
  --lilac:#ead6f1;
  --row-light:#f2f1f1;
  --row-dark:#e0dfdf;
  --panel:#f8f8f8;
  --field-line:#b9b9b9;
  --muted:#6b6b6b;
  --white:#ffffff;
  --gold:#e8c98a;
}
*{box-sizing:border-box;margin:0;padding:0}
html,body{width:717px;height:1200px;overflow:hidden;background:var(--white)}
body{position:relative;font-family:'Poppins',sans-serif;color:var(--ink)}

.site-header{position:absolute;left:0;top:0;width:717px;height:54px;background:var(--header)}
.brand{position:absolute;display:flex;align-items:center;gap:5px;font-family:'Lato',sans-serif;font-weight:700;color:var(--blue);white-space:nowrap}
.site-header .brand{left:146px;top:18px;font-size:15px}
.brand-mark{width:12px;height:12px;background:var(--blue)}
.account-tabs{position:absolute;left:460px;top:0;height:14px;display:flex;font-family:'Lato',sans-serif;font-size:6.5px;color:var(--white)}
.account-tabs span{display:flex;align-items:center;gap:3px;padding:0 12px}
.tab-login{background:#4a4a4a;border-bottom-left-radius:8px}
.tab-signup{background:var(--blue);border-bottom-right-radius:8px}
.phone-badge{position:absolute;left:434px;top:26px;width:17px;height:17px;border-radius:50%;background:var(--blue);display:flex;align-items:center;justify-content:center}
.header-divider{position:absolute;left:458px;top:24px;width:1px;height:22px;background:#666}
.office-lines{position:absolute;left:467px;top:25px;font-family:'Lato',sans-serif;font-size:8px;line-height:10.5px;color:var(--white)}
.office-lines b{font-weight:700}

.main-nav{position:absolute;left:0;top:54px;width:717px;height:19px;background:var(--blue);font-family:'Lato',sans-serif;font-size:6.5px;color:var(--white)}
.main-nav a{position:absolute;top:6px;color:inherit;text-decoration:none}

.page-hero{position:absolute;left:0;top:73px;width:717px;height:55px;background:linear-gradient(100deg,#858aab 0%,#a9a3c3 40%,#d9b8c6 70%,#f5c49f 100%)}
.page-hero h1{position:absolute;width:100%;top:21px;text-align:center;font-family:'Lato',sans-serif;font-weight:400;font-size:12px;color:var(--white)}

.pricing{position:absolute;left:120px;top:128px;width:477px;display:grid;grid-template-columns:156px 157px 157px;column-gap:3.5px}
.plan-head{height:80px;color:var(--white);text-align:center;font-family:'Montserrat',sans-serif}
.features-head{background:var(--lilac);color:var(--ink);display:flex;align-items:center;justify-content:center;font-weight:700;font-size:12px}
.plan-carte{background:var(--blue)}
.plan-unlimited{background:var(--navy)}
.plan-title{font-size:12.5px;font-weight:700;margin-top:8px}
.plan-sub{font-size:6.4px;font-family:'Poppins',sans-serif;margin-top:1px}
.plan-prices{display:flex;margin-top:9px;font-family:'Poppins',sans-serif}
.plan-prices div{flex:1;border-left:1px solid rgba(255,255,255,.35);line-height:1}
.plan-prices div:first-child{border-left:0}
.plan-prices strong{display:block;font-weight:400;font-size:11.5px}
.plan-prices small{font-size:5.6px}
.cell{height:18.7px;display:flex;align-items:center;font-size:5.8px}
.cell.tick{justify-content:center}
.cell.feature{padding-left:13px;gap:6px}
.cell.feature::before{content:"";width:5px;height:5px;border:1px solid var(--ink);border-radius:50%}
.odd{background:var(--row-light)}
.even{background:var(--row-dark)}

.signup-panel{position:absolute;left:120px;top:510px;width:477px;height:437px;background:var(--panel)}
.signup-bar{position:absolute;left:4px;top:8px;width:469px;height:29px;background:var(--ink);color:var(--white);display:flex;align-items:center;justify-content:center;font-family:'Montserrat',sans-serif;font-weight:700;font-size:12px;letter-spacing:.3px}
.billing-note{position:absolute;top:47px;width:100%;text-align:center;font-size:6px;color:#333}
.form-group-title{position:absolute;left:46px;width:384px;display:flex;align-items:flex-end;gap:3px;font-size:6px;font-weight:500;letter-spacing:.2px}
.form-group-title::after{content:"";flex:1;height:0;border-bottom:1px solid #555;margin-bottom:2px}
.field{position:absolute;width:187px;height:18px;border:1px solid var(--field-line);background:var(--white);font-family:'Poppins',sans-serif;font-size:5.6px;padding:0 3px;color:var(--muted)}
.field::placeholder{color:var(--muted)}
.col-a{left:45px}
.col-b{left:243px}
.submit-btn{position:absolute;left:145px;top:404px;width:187px;height:18px;background:var(--blue);border:0;color:var(--white);font-family:'Montserrat',sans-serif;font-weight:600;font-size:6px;letter-spacing:.5px}

.site-footer{position:absolute;left:0;top:947px;width:717px;height:235px;background:var(--footer);font-family:'Lato',sans-serif;color:#d8d8d8}
.footer-heading{position:absolute;top:18px;font-size:8px;color:var(--white);font-weight:400}
.quick-links{position:absolute;left:146px;top:36px;list-style:none;font-size:6px;line-height:12px}
.quick-links li::before{content:"›";margin-right:4px}
.quick-links .highlight{color:var(--gold)}
.footer-divider{position:absolute;top:15px;width:1px;height:108px;background:#333}
.contact-block{position:absolute;left:291px;top:34px;font-size:5.4px;line-height:8px}
.contact-block b{color:var(--white)}
.contact-line{display:flex;gap:5px}
.site-footer .brand{left:474px;top:22px;font-size:10px}
.site-footer .brand-mark{width:8px;height:8px}
.socials{position:absolute;left:492px;top:38px;display:flex;gap:4px}
.socials span{width:12.5px;height:12.5px;border-radius:50%}
.copyright{position:absolute;left:0;top:1182px;width:717px;height:18px;background:var(--footer-base);color:var(--white);font-family:'Lato',sans-serif;font-size:5.8px;text-align:center;line-height:18px}
</style>
</head>
<body>
<svg width="0" height="0" style="position:absolute">
  <symbol id="tick" viewBox="0 0 20 20"><circle cx="10" cy="10" r="8.5" fill="none" stroke="#1c1c1c" stroke-width="1.8"/><path d="M6 10.2l2.8 2.8L14.2 7.5" fill="none" stroke="#1c1c1c" stroke-width="1.9" stroke-linecap="round" stroke-linejoin="round"/></symbol>
</svg>

<header class="site-header">
  <div class="brand"><span class="brand-mark"></span>Bright Loom Rewards</div>
  <div class="account-tabs">
    <span class="tab-login">
      <svg width="6" height="6" viewBox="0 0 10 10"><path d="M1 5h6M5 2.5L7.5 5 5 7.5M7 1h2v8H7" fill="none" stroke="#fff" stroke-width="1.3"/></svg>LOGIN</span>
    <span class="tab-signup">
      <svg width="7" height="6" viewBox="0 0 12 10"><circle cx="4" cy="3" r="2.3" fill="#fff"/><path d="M0 10c0-3 2-4.5 4-4.5S8 7 8 10z" fill="#fff"/><path d="M10 3v4M8 5h4" stroke="#fff" stroke-width="1.2"/></svg>SIGN UP</span>
  </div>
  <div class="phone-badge"><svg width="8" height="8" viewBox="0 0 10 10"><path d="M2.2 1l1.5 2-1 1c.6 1.3 1.5 2.2 2.8 2.8l1-1 2 1.5-.8 1.5C4.5 8.8 1.2 5.5 1 1.8z" fill="#fff"/></svg></div>
  <div class="header-divider"></div>
  <div class="office-lines">USA Office : <b>555-204-3187</b><br>International : <b>1-800-555-0142</b></div>
</header>

<nav class="main-nav">
  <a style="left:164px">HOME</a><a style="left:209px">OUR INCENTIVES</a><a style="left:283px">SAMPLES</a><a style="left:336px">AFFILIATES</a><a style="left:394px">TESTIMONIALS</a><a style="left:462px">FAQ</a><a style="left:500px">CONTACT</a>
</nav>

<section class="page-hero" role="img" aria-label="Soft sunset sky banner behind the page title"><h1>SIGN UP</h1></section>

<section class="pricing">
  <div class="plan-head features-head">FEATURES</div>
  <div class="plan-head plan-carte">
    <div class="plan-title">Al A Carte Program</div>
    <div class="plan-sub">1 Certificate Type Each Month</div>
    <div class="plan-prices"><div><strong>$49</strong><small>per month</small></div><div><strong>$239</strong><small>for 6 months</small></div><div><strong>$399</strong><small>for 12 months</small></div></div>
  </div>
  <div class="plan-head plan-unlimited">
    <div class="plan-title">Unlimited Program</div>
    <div class="plan-sub">Unlimited Amounts Of All The Certificates</div>
    <div class="plan-prices"><div><strong>$49</strong><small>per month</small></div><div><strong>$495</strong><small>for 6 months</small></div><div><strong>$2,295</strong><small>for 12 months</small></div></div>
  </div>

  <div class="cell feature odd">Unlimited certificate pdf downloads</div><div class="cell tick odd"><svg width="11" height="11"><use href="#tick"/></svg></div><div class="cell tick odd"><svg width="11" height="11"><use href="#tick"/></svg></div>
  <div class="cell feature even">Unlimited e-mail certificates</div><div class="cell tick even"><svg width="11" height="11"><use href="#tick"/></svg></div><div class="cell tick even"><svg width="11" height="11"><use href="#tick"/></svg></div>
  <div class="cell feature odd">Unlimited text/sms certificates</div><div class="cell tick odd"><svg width="11" height="11"><use href="#tick"/></svg></div><div class="cell tick odd"><svg width="11" height="11"><use href="#tick"/></svg></div>
  <div class="cell feature even">Unlimited api usage</div><div class="cell tick even"><svg width="11" height="11"><use href="#tick"/></svg></div><div class="cell tick even"><svg width="11" height="11"><use href="#tick"/></svg></div>
  <div class="cell feature odd">Unlimited web banner certificates</div><div class="cell tick odd"><svg width="11" height="11"><use href="#tick"/></svg></div><div class="cell tick odd"><svg width="11" height="11"><use href="#tick"/></svg></div>
  <div class="cell feature even">Full redemption tracking</div><div class="cell tick even"><svg width="11" height="11"><use href="#tick"/></svg></div><div class="cell tick even"><svg width="11" height="11"><use href="#tick"/></svg></div>
  <div class="cell feature odd">Certificate distribution reports</div><div class="cell tick odd"><svg width="11" height="11"><use href="#tick"/></svg></div><div class="cell tick odd"><svg width="11" height="11"><use href="#tick"/></svg></div>
  <div class="cell feature even">White label redemption site</div><div class="cell tick even"><svg width="11" height="11"><use href="#tick"/></svg></div><div class="cell tick even"><svg width="11" height="11"><use href="#tick"/></svg></div>
  <div class="cell feature odd">End user marketing videos</div><div class="cell tick odd"><svg width="11" height="11"><use href="#tick"/></svg></div><div class="cell tick odd"><svg width="11" height="11"><use href="#tick"/></svg></div>
  <div class="cell feature even">Marketing posters and flyers</div><div class="cell tick even"><svg width="11" height="11"><use href="#tick"/></svg></div><div class="cell tick even"><svg width="11" height="11"><use href="#tick"/></svg></div>
  <div class="cell feature odd">Product descriptioni brochures</div><div class="cell tick odd"><svg width="11" height="11"><use href="#tick"/></svg></div><div class="cell tick odd"><svg width="11" height="11"><use href="#tick"/></svg></div>
  <div class="cell feature even">The latest tips</div><div class="cell tick even"><svg width="11" height="11"><use href="#tick"/></svg></div><div class="cell tick even"><svg width="11" height="11"><use href="#tick"/></svg></div>
  <div class="cell feature odd">Seperate redemption websites</div><div class="cell tick odd"><svg width="11" height="11"><use href="#tick"/></svg></div><div class="cell tick odd"><svg width="11" height="11"><use href="#tick"/></svg></div>
  <div class="cell feature even">Contact us 24/7</div><div class="cell tick even"><svg width="11" height="11"><use href="#tick"/></svg></div><div class="cell tick even"><svg width="11" height="11"><use href="#tick"/></svg></div>
  <div class="cell feature odd">Affiliate program</div><div class="cell tick odd"><svg width="11" height="11"><use href="#tick"/></svg></div><div class="cell tick odd"><svg width="11" height="11"><use href="#tick"/></svg></div>
  <div class="cell feature even">Discount travel booking engine</div><div class="cell tick even"><svg width="11" height="11"><use href="#tick"/></svg></div><div class="cell tick even"><svg width="11" height="11"><use href="#tick"/></svg></div>
</section>

<form class="signup-panel">
  <div class="signup-bar">SIGN UP</div>
  <p class="billing-note">**The information you provide below must match the billing details of where your billing statement is mailed to from your bank.</p>

  <div class="form-group-title" style="top:79px">PERSONAL INFORMATION</div>
  <input class="field col-a" style="top:98px" placeholder="*First Name">
  <input class="field col-b" style="top:98px" placeholder="*Last Name">
  <input class="field col-a" style="top:124px" placeholder="*Phone">
  <input class="field col-b" style="top:124px" placeholder="*Email Address">
  <input class="field col-a" style="top:149px" placeholder="*Company Name">
  <input class="field col-b" style="top:149px" placeholder="*Industry">
  <input class="field col-a" style="top:176px" placeholder="*Billing Address 1">
  <input class="field col-b" style="top:176px" placeholder="*Billing Address 2">
  <input class="field col-a" style="top:201px" placeholder="*City">
  <input class="field col-b" style="top:201px" placeholder="*State">
  <input class="field col-a" style="top:228px" placeholder="*Zip">
  <input class="field col-b" style="top:228px" placeholder="*Country">

  <div class="form-group-title" style="top:261px">USER INFORMATION</div>
  <input class="field col-a" style="top:278px" placeholder="*User Name">
  <input class="field col-b" style="top:278px" placeholder="*Password">
  <input class="field col-a" style="top:303px" placeholder="*Confirm Password">
  <input class="field col-b" style="top:303px" placeholder="*First Name">

  <div class="form-group-title" style="top:349px">OTHER INFORMATION</div>
  <input class="field col-a" style="top:366px" placeholder="*How Did You Hear About Us?">
  <input class="field col-b" style="top:366px" placeholder="*Promocode">

  <button class="submit-btn" type="button">SUBMIT</button>
</form>

<footer class="site-footer">
  <h3 class="footer-heading" style="left:146px">QUICK LINKS</h3>
  <ul class="quick-links">
    <li>Home</li><li>Our Incentives</li><li>Samples</li><li>Affiliate</li><li>Testimonials</li><li class="highlight">Faq</li><li>Contact Us</li><li>Terms &amp; Conditions</li><li>Privacy Policy</li><li>Hoteliers</li><li>BLR PDF Flyer</li><li>BLR PDF Brochure</li><li>BLR Certificates List</li><li>How To Use BLR Certificates</li><li>Free Video Ad Mock Up For Marketing</li>
  </ul>
  <div class="footer-divider" style="left:280px"></div>
  <h3 class="footer-heading" style="left:291px">CONTACT DETAILS</h3>
  <div class="contact-block">
    <div class="contact-line"><svg width="6" height="7" viewBox="0 0 10 12"><path d="M5 0a4 4 0 014 4c0 3-4 8-4 8S1 7 1 4a4 4 0 014-4z" fill="#d8d8d8"/><circle cx="5" cy="4" r="1.5" fill="#1d1d1d"/></svg><div><b>Bright Loom Rewards Group, Inc.</b><br>1470 Harbor View Lane<br>Bayside CA 90210</div></div>
    <div class="contact-line" style="margin-top:16px"><svg width="7" height="7" viewBox="0 0 10 10"><rect x="0.5" y="1.5" width="9" height="8" fill="none" stroke="#d8d8d8"/><path d="M0.5 4h9M3 0v3M7 0v3" stroke="#d8d8d8"/></svg><div>Hours: Mon-Fri 8am - 5pm PST<br>Sat-Sun CLOSED</div></div>
  </div>
  <div class="footer-divider" style="left:467px"></div>
  <div class="brand"><span class="brand-mark"></span>Bright Loom Rewards</div>
  <div class="socials">
    <span style="background:#2c4a8f"></span><span style="background:#e13b22"></span><span style="background:#1b66ad"></span><span style="background:#3a8ee6"></span>
  </div>
</footer>
<div class="copyright">Copyright 2005-2020 Bright Loom Rewards Group, Inc. All Rights Reserved.</div>
</body>
</html>
```